Football and Sports Management Agency Stationary

We have a logo, fonts, website and colour palette.
We need the logo refined by a proper designer and then business stationary designed. You can see on the website how it needs adjusting by a designers eye.
The company is a high end sports management company aiming to attract and represent professional athletes. The name Velorin is to indicate a 'Constellation of Stars' ie our clients. The dots on the star should be slightly different sizes to reflect that some clients will be bigger than others.
Colours:
#e6e6e6
#edd2a4
#caaa72 (main gold and also used on site)
#3f3f42
#001d38
#edeced (on website)
#191c23 (on website)
Font:
QT (velorin)
QT Melbrook (sports management)
We would like:
- Letterhead (word and indesign and PDF print format). I have attached an example for one I like. It's quiet a clean design with the contact details and address taking up only a small amount of room.
- Business card (dark on the back with the logo, personal details on the front). Only needs name, title, email, website and phone number. No company address (in PDF and indesign format)
- Powerpoint slide theme
- Logo in vector format for light and dark versions and single colour versions. And optimised web version
- Simple brand guide PDF showing colour, font and logo (a one/two page PDF)
Any questions, please ask.
NEW INFO:
Contact Details
Maren Solwick
Director
Mobile: +44 7630 218 977
Phone: +44 0113 872 604
Email: maren@velorinathletic.example
Web: velorinathletic.example
Corran Lodge, 14 Mill Bank Road, Stockport, SK4 9TW
Company number 40718362
Target Market(s)
Professional athletes, professional sports teams.
Industry/Entity Type
Management
Requirements
Must have
- NEW
- The designs must look cool, classy and high quality. My suggestion for this is to keep the text small and precise with uncomplicated design.
Nice to have
- Application of brand displayed on stationary and additional pieces of stationary branded.
- Draw some inspiration from the website. eg the slant angles used separate the sections.
Should not have
- Don't create new logos etc.

```html
<!DOCTYPE html>
<html lang="en">
<head>
<meta charset="utf-8">
<title>Velorin Stationery</title>
<link rel="stylesheet" href="https://fonts.googleapis.com/css2?family=Josefin+Sans:wght@300&family=PT+Serif&display=swap">
<style>
  :root {
    --canvas: #e6e6e6;
    --ink: #0a0a0a;
    --paper: #ffffff;
    --gold: #caaa72;
    --light: #edeced;
    --rule: #3f3f42;
  }
  * { margin: 0; padding: 0; box-sizing: border-box; }
  html, body { width: 1200px; height: 1200px; overflow: hidden; background: var(--canvas); }
  .stage { position: relative; width: 1200px; height: 1200px; }

  .wordmark {
    font-family: "Josefin Sans", sans-serif;
    font-weight: 300;
    color: var(--light);
    text-transform: uppercase;
    letter-spacing: 0.32em;
    white-space: nowrap;
    line-height: 1;
  }
  .contact { font-family: "PT Serif", serif; white-space: nowrap; line-height: 1; }
  .icon { display: block; flex: none; }

  /* Letterhead */
  .letterhead {
    position: absolute; left: 183px; top: 118px; width: 754px; height: 975px;
    background: var(--paper);
  }
  .letterhead-band {
    position: absolute; left: 0; top: 0; width: 100%; height: 120px; background: var(--ink);
  }
  .letterhead-band .wordmark { position: absolute; left: 27px; top: 72px; font-size: 20px; }
  .letterhead-contacts {
    position: absolute; right: 33px; top: 26px;
    display: flex; flex-direction: column; align-items: flex-end; gap: 7px;
  }
  .letterhead-contacts .line {
    display: flex; align-items: center; gap: 9px;
    color: var(--gold); font-size: 15px; height: 16px;
  }

  /* Business cards */
  .card { position: absolute; background: var(--ink); }
  .card-front { left: 649px; top: 374px; width: 406px; height: 232px; }
  .card-back { left: 649px; top: 645px; width: 405px; height: 231px; }

  .card-front .wordmark { position: absolute; left: 84px; top: 129px; font-size: 17px; }
  .card-divider { position: absolute; left: 207px; top: 74px; width: 1px; height: 85px; background: var(--rule); }
  .card-person { position: absolute; left: 219px; top: 77px; }
  .card-name { font-family: "PT Serif", serif; color: var(--gold); font-size: 14px; line-height: 1; }
  .card-title { font-family: "PT Serif", serif; color: var(--light); font-size: 10px; margin-top: 5px; line-height: 1; }
  .card-contacts { position: absolute; left: 219px; top: 113px; display: flex; flex-direction: column; gap: 4px; }
  .card-contacts .line { display: flex; align-items: center; gap: 7px; color: var(--light); font-size: 9.5px; height: 11px; }

  .card-back .wordmark { position: absolute; left: 0; width: 100%; top: 130px; text-align: center; font-size: 24px; padding-left: 0.32em; }
</style>
</head>
<body>
<main class="stage">

  <section class="letterhead" aria-label="Letterhead">
    <header class="letterhead-band">
      <div class="wordmark">Velorin</div>
      <div class="letterhead-contacts">
        <div class="line contact">+44 0113 872 604
          <svg class="icon" width="16" height="16" viewBox="0 0 16 16"><rect width="16" height="16" rx="3" fill="#fff"/><path d="M4 6.5c0-1.5 1.8-2.3 4-2.3s4 .8 4 2.3v.8H10.2v-1H5.8v1H4z M5.5 8h5l1 4h-7z" fill="#0a0a0a"/><circle cx="8" cy="10" r="1.1" fill="#fff"/></svg>
        </div>
        <div class="line contact">velorinathletic.example
          <svg class="icon" width="16" height="16" viewBox="0 0 16 16"><rect width="16" height="16" rx="3" fill="#fff"/><g fill="none" stroke="#0a0a0a" stroke-width="1"><circle cx="8" cy="8" r="4.6"/><ellipse cx="8" cy="8" rx="2" ry="4.6"/><path d="M3.4 8h9.2M4 5.7h8M4 10.3h8"/></g></svg>
        </div>
        <div class="line contact">maren@velorinathletic.example
          <svg class="icon" width="16" height="16" viewBox="0 0 16 16"><rect width="16" height="16" rx="3" fill="#fff"/><rect x="3.5" y="5" width="9" height="6.5" fill="#0a0a0a"/><path d="M3.8 5.3 8 8.6l4.2-3.3" fill="none" stroke="#fff" stroke-width=".9"/></svg>
        </div>
      </div>
    </header>
  </section>

  <section class="card card-front" aria-label="Business card, front">
    <div class="wordmark">Velorin</div>
    <div class="card-divider"></div>
    <div class="card-person">
      <div class="card-name">Maren Solwick</div>
      <div class="card-title">Director</div>
    </div>
    <div class="card-contacts">
      <div class="line contact">
        <svg class="icon" width="10" height="10" viewBox="0 0 16 16"><rect width="16" height="16" rx="3" fill="#fff"/><path d="M4 6.5c0-1.5 1.8-2.3 4-2.3s4 .8 4 2.3v.8H10.2v-1H5.8v1H4z M5.5 8h5l1 4h-7z" fill="#0a0a0a"/></svg>
        +44 0113 872 604</div>
      <div class="line contact">
        <svg class="icon" width="10" height="10" viewBox="0 0 16 16"><rect width="16" height="16" rx="3" fill="#fff"/><g fill="none" stroke="#0a0a0a" stroke-width="1.3"><circle cx="8" cy="8" r="4.6"/><path d="M3.4 8h9.2M8 3.4v9.2"/></g></svg>
        velorinathletic.example</div>
      <div class="line contact">
        <svg class="icon" width="10" height="10" viewBox="0 0 16 16"><rect width="16" height="16" rx="3" fill="#fff"/><rect x="3.5" y="5" width="9" height="6.5" fill="#0a0a0a"/></svg>
        maren@velorinathletic.example</div>
    </div>
  </section>

  <section class="card card-back" aria-label="Business card, back">
    <div class="wordmark">Velorin</div>
  </section>

</main>
</body>
</html>
```